Tin Lantern Drift

We are a group of students studying abroad at Uni in Lennox Head, Australia. For a crowd sourcing project we are working on we need help creating and making a website and/or Friendwall app. None of us have any background in web making or code writing. Our idea is to get as many people around the world to hug random people in any manner and post them to our site or app. Also we would bring in photos. We are in the midst of creating a statement plan that will be on a card given to people that we hug so they can go see the site and see their photo/video. We also want them to take the idea and pass it along to other so we can have a dynamic growing webpage and product. We have money available to start this project immediately. We are not behind but very close to our end point of the project and time here in Lennox. I do have all of the ideas and thoughts together already. If there is a way we could speak other than email please let me know. Thank you!
Updates

Reason: Still doing great work on it! Lets just get finalized plans and well launch the site! Thanks

Target Market(s)

Anyone. In particular university students because we are the ones that are most likely to break out of our shells to hug randomly.

Industry/Entity Type

Crowd

Requirements
Must have
• Photo and video albums that will update when people post them.
We also need a map that can pinpoint where people have hugged around the world. Also just a basic banner/headpage and web design. We are not looking for it to be anything incredible we simply need to have a project created and up and running before we go. Amount of people doesn't matter.

```html
<!DOCTYPE html>
<html lang="en">
<head>
<meta charset="utf-8">
<title>Tin Lantern Drift</title>
<link rel="stylesheet" href="https://fonts.googleapis.com/css2?family=Overlock:ital,wght@0,400;0,700;1,400&display=swap">
<style>
:root{
  --page:#f0f0f0;
  --ink:#333333;
  --ink-soft:#555555;
  --brand:#e05a5a;
  --bar:#9a9a9a;
  --frame:#e4e4e4;
  --frame-edge:#bcbcbc;
  --footer:#333333;
  --footer-ink:#bdbdbd;
  --sky:#7fb3dd;
  --trees:#5f8a4a;
  --paving:#9c8a80;
}
*{margin:0;padding:0;box-sizing:border-box}
html,body{width:760px;height:1200px;overflow:hidden;background:var(--page)}
body{position:relative;font-family:"Overlock",sans-serif;font-style:italic;color:var(--ink-soft)}
.heading{font-family:"Overlock",sans-serif;font-style:normal;font-weight:700;color:var(--ink);text-shadow:1px 2px 2px rgba(0,0,0,.25);white-space:nowrap}
.brand{position:absolute;left:56px;top:18px;display:flex;align-items:center;gap:14px}
.brand-dot{width:30px;height:30px;border-radius:50%;background:var(--brand)}
.brand-name{font-family:"Overlock",sans-serif;font-style:normal;font-weight:700;font-size:21px;color:var(--brand)}
.login{position:absolute;left:378px;top:0;width:268px;height:33px;background:var(--bar);border-radius:0 0 3px 3px;box-shadow:0 2px 4px rgba(0,0,0,.3);display:flex;align-items:center;padding-left:17px;gap:13px}
.login-field{width:85px;height:15px;background:#fff;border:1px solid #666;border-radius:2px;font-size:11px;color:#aaa;text-align:center;line-height:13px}
.login-button{font-style:normal;font-size:15px;color:#333;margin-left:3px}
.nav{position:absolute;top:50px;left:0;width:760px;font-size:20px;color:#444}
.nav a{position:absolute;color:inherit;text-decoration:none}
.slider{position:absolute;left:81px;top:101px;width:609px;height:382px;background:var(--frame);border:1px solid var(--frame-edge);box-shadow:0 2px 5px rgba(0,0,0,.2)}
.slide{position:absolute;left:23px;top:17px;width:563px;height:347px;background:linear-gradient(180deg,var(--sky) 0%,#b9d3e8 28%,var(--trees) 34%,#8aa071 44%,var(--paving) 50%,#8d7c72 100%)}
.slider-arrow{position:absolute;top:151px;width:39px;height:88px;background:var(--frame)}
.slider-arrow.prev{left:23px}
.slider-arrow.next{left:546px}
.slider-arrow svg{position:absolute;left:12px;top:30px}
.quote{position:absolute;top:502px;width:760px;text-align:center;font-size:29px;white-space:nowrap}
.column{position:absolute;top:562px;width:240px}
.column h2{font-size:31px;margin-bottom:5px}
.column p{font-size:17px;line-height:21.8px;color:#444;white-space:nowrap}
.col-left{left:44px;text-align:left}
.col-mid{left:263px;text-align:center}
.col-right{left:490px;text-align:right}
.divider{position:absolute;top:852px;left:0;width:760px;border-top:1px dashed #999}
.join-title{position:absolute;left:38px;top:861px;font-size:41px}
.join-copy{position:absolute;left:16px;top:910px;font-size:28px;line-height:35px;color:#444;white-space:nowrap}
.handout{position:absolute;left:92px;top:1006px;font-size:41px;color:var(--ink-soft)}
.download{position:absolute;left:578px;top:1013px;width:139px;height:34px;border-radius:17px;background:linear-gradient(#5d6166,#3a3d41);border:1px solid #222;color:#fff;font-style:normal;font-weight:700;font-size:18px;text-align:center;line-height:31px}
.social-title{position:absolute;top:1092px;width:760px;text-align:center;font-size:30px;color:#333}
.social{position:absolute;top:1136px;width:760px;display:flex;justify-content:center;gap:12px;font-size:14px;color:#444}
.footer{position:absolute;left:0;top:1172px;width:760px;height:28px;background:var(--footer);color:var(--footer-ink);text-align:center;font-size:19px;line-height:27px}
</style>
</head>
<body>
<header>
  <div class="brand"><span class="brand-dot"></span><span class="brand-name">Tin Lantern Drift</span></div>
  <form class="login">
    <span class="login-field">Username</span>
    <span class="login-field">Password</span>
    <span class="login-button">Log In</span>
  </form>
  <nav class="nav">
    <a style="left:350px">Home</a>
    <a style="left:428px">Photos</a>
    <a style="left:516px">Videos</a>
    <a style="left:606px">Map</a>
  </nav>
</header>

<section class="slider">
  <div class="slide" role="img" aria-label="Photo of two people hugging in a paved city square under a blue sky"></div>
  <div class="slider-arrow prev"><svg width="14" height="28" viewBox="0 0 14 28"><path d="M14 0V28L0 14Z" fill="#333"/></svg></div>
  <div class="slider-arrow next"><svg width="14" height="28" viewBox="0 0 14 28"><path d="M0 0V28L14 14Z" fill="#333"/></svg></div>
</section>

<p class="quote">"Life begins at the edge of your comfort zone."</p>

<section class="column col-left">
  <h2 class="heading">What We Do</h2>
  <p>Stormcats food truck 8-bit,<br>synth gentrify harbor<br>apparel cillum biodiesel.<br>Bicycle rights nulla mustache<br>ut laborum. Ashgrove<br>brunch squid jean shorts,<br>3 fox dusk aute scenester<br>ethnic do hella polaroid<br>single-origin coffee.</p>
</section>
<section class="column col-mid">
  <h2 class="heading">How We Do It</h2>
  <p>Stormcats food truck 8-bit,<br>synth gentrify harbor<br>apparel cillum biodiesel.<br>Bicycle rights nulla mustache<br>ut laborum. Ashgrove<br>brunch squid jean shorts,<br>3 fox dusk aute scenester<br>ethnic do hella polaroid<br>single-origin coffee.</p>
</section>
<section class="column col-right">
  <h2 class="heading">When We Do IT</h2>
  <p>Stormcats food truck 8-bit,<br>synth gentrify harbor<br>apparel cillum biodiesel.<br>Bicycle rights nulla mustache<br>ut laborum. Ashgrove<br>brunch squid jean shorts,<br>3 fox dusk aute scenester<br>ethnic do hella polaroid<br>single-origin coffee.</p>
</section>

<div class="divider"></div>
<h2 class="heading join-title">Join The Movement.</h2>
<p class="join-copy">&nbsp;Marlowe's locavore keffiyeh, sapiente art party vice<br>DIY selvage master cleanse lomo quis butcher.</p>
<h2 class="heading handout">Download Our Hand-out</h2>
<span class="download">Download</span>

<p class="social-title">Join us on</p>
<div class="social"><span>Friendwall</span><span>Chirpline</span><span>Orbitpal</span><span>Clipstream</span></div>

<footer class="footer">©2012 Tin Lantern Drift All Rights Reserved</footer>
</body>
</html>
```